Modern labels for Murlane products

We need a new design of our labels for the product “Murlane” (https://www.murlane-example.eu/#) . The reason why we want to change our labels is to get a modern and more advanced look of our product. We also want to create a unique product that is attractive for our customers, even if the product are used in hospitals and healthcare centers for collecting dangerous waste.

There is three sizes of labels (55x95, 90x95, 170x95 mm) for different boxes, but the label will contain similar information. There are certain requirements and factors from regulations/standards that you need to follow when you create the new layout. But it’s up to you to change the design. You can work with background, fonts, effects, colors, structure, pattern, new symbols, logotype etc. The label could be any color, but the container will stay yellow so they have to look good together.

Keywords: Elegant, modern, functional, attractive, exclusive

Target Market(s)

Hospitals and healthcare centers

Industry/Entity Type

Product

Font styles to use
Serif
Sans Serif

Colors

Designer to choose colors to be used in the design.

Requirements
Must have
• Requirements for the regulations ADR UN3291 and ISO 23907 (PDF).
• * Symbol for danger waste
• * Filling level
• * "Danger"
• * Symbol for no second use
• * Symbol for manufaturer
• * Referencenumber
• * Text "”Clinical waste, Unspecified, N.O.S.”"
• * Area for series, certification, size and useful capacity
• * Area for Illustrations.
• * Text “Autoclavable at 134 c”, “Do not force closure” and “Do not overfill”.
• * Text for certification ”UN 3291 1H2/Y0,3/S/YR/N/QVK7148B”
• Three different sizes (55x95, 90x95, 170x95).
• More info in PDF "3kravspecifikation"
Nice to have
• A modern, elegant, advanced look of our label.
Should not have
• The information must be clear and readable, not too decorative/handwriting fonts.

```html
<!DOCTYPE html>
<html lang="en">
<head>
<meta charset="utf-8">
<title>Murlane clinical waste label</title>
<link rel="stylesheet" href="https://fonts.googleapis.com/css2?family=Oswald:wght@400;500;600;700&family=Roboto+Slab:wght@700;800&family=Roboto+Condensed:ital,wght@0,400;0,700;1,400&display=swap">
<style>
  :root {
    --page: #ffffff;
    --yellow-light: #fbdc3a;
    --yellow-deep: #f2b632;
    --red: #e0202e;
    --red-dark: #b8141f;
    --ink: #1d1d1d;
    --white: #ffffff;
    --panel-grey: #d8d8d8;
  }
  * { margin: 0; padding: 0; box-sizing: border-box; }
  html, body { width: 1200px; height: 1097px; overflow: hidden; background: var(--page); }
  .label {
    position: absolute; left: 100px; top: 198px; width: 1000px; height: 700px;
    background: linear-gradient(160deg, var(--yellow-light), var(--yellow-deep));
    border-radius: 10px; overflow: hidden;
    font-family: "Oswald", sans-serif; color: var(--ink);
  }
  .label-shapes { position: absolute; inset: 0; }
  .filling-level {
    position: absolute; left: 150px; top: 30px; width: 700px; height: 26px; text-align: center;
    font-family: "Oswald", sans-serif; font-weight: 600; font-size: 18px;
    letter-spacing: 12px; color: var(--yellow-light); line-height: 26px;
  }
  .brand {
    position: absolute; left: 44px; top: 112px; display: flex; align-items: center; gap: 10px;
    font-family: "Oswald", sans-serif; font-weight: 600; font-size: 46px; line-height: 1.2; color: var(--ink);
  }
  .brand-mark { width: 22px; height: 22px; background: var(--ink); }
  .un-number {
    position: absolute; right: 44px; top: 86px; text-align: right;
    font-family: "Oswald", sans-serif; font-weight: 700; font-size: 64px; line-height: 1; letter-spacing: 2px;
  }
  .un-code {
    position: absolute; right: 44px; top: 160px;
    font-family: "Roboto Condensed", sans-serif; font-size: 17px; color: var(--ink);
  }
  .waste-title {
    position: absolute; left: 44px; top: 410px;
    font-family: "Oswald", sans-serif; font-weight: 600; font-size: 40px; line-height: 1.2; color: var(--white);
  }
  .diamond-text {
    position: absolute; left: 330px; top: 130px; width: 300px; text-align: center;
  }
  .biohazard {
    width: 86px; height: 86px; border-radius: 50%; background: var(--ink); margin: 0 auto 12px;
  }
  .danger {
    font-family: "Oswald", sans-serif; font-weight: 700; font-size: 44px; line-height: 1; color: var(--red);
  }
  .substance {
    font-family: "Roboto Slab", serif; font-weight: 800; font-size: 18px; line-height: 1.2; margin-top: 6px;
  }
  .notice {
    font-family: "Roboto Condensed", sans-serif; font-size: 14px; line-height: 1.25; margin-top: 4px;
  }
  .hazard-class {
    font-family: "Oswald", sans-serif; font-weight: 600; font-size: 36px; line-height: 1; margin-top: 4px;
  }
  .no-reuse {
    position: absolute; right: 40px; top: 356px; text-align: right; color: var(--white);
    font-family: "Oswald", sans-serif; font-weight: 700;
  }
  .no-reuse .no { font-size: 72px; line-height: 1; }
  .no-reuse .second-use { font-size: 26px; line-height: 1.1; }
  .instructions {
    position: absolute; left: 40px; top: 520px; width: 400px; height: 160px;
    display: grid; grid-template-columns: 1fr 1fr 1fr 1fr; gap: 6px;
  }
  .instruction-step {
    position: relative; background: var(--white); border: 2px solid var(--ink); border-radius: 3px;
  }
  .instruction-step span {
    position: absolute; left: 5px; top: 2px; font-family: "Roboto Condensed", sans-serif; font-size: 14px; font-weight: 700;
  }
  .instruction-art { position: absolute; left: 10px; right: 10px; top: 26px; bottom: 12px; background: var(--panel-grey); }
  .specs {
    position: absolute; left: 480px; top: 530px; width: 480px; padding: 8px 12px;
    background: var(--white); border-radius: 4px;
    font-family: "Roboto Condensed", sans-serif; font-size: 14px; line-height: 1.5;
  }
  .specs-row { display: flex; justify-content: space-between; }
  .specs-row em { font-style: italic; }
  .maker {
    position: absolute; left: 480px; top: 604px; width: 480px; height: 76px; display: flex; gap: 12px;
  }
  .maker-brand {
    width: 150px; display: flex; align-items: center; gap: 8px; color: var(--white);
    font-family: "Oswald", sans-serif; font-weight: 600; font-size: 22px;
  }
  .maker-mark { width: 14px; height: 14px; background: var(--white); }
  .maker-fields {
    flex: 1; background: var(--white); border-radius: 4px; padding: 4px 12px;
    font-family: "Roboto Condensed", sans-serif; font-size: 13px;
  }
  .maker-fields div { border-bottom: 1px solid var(--ink); height: 22px; line-height: 22px; }
  .maker-fields div:last-child { border-bottom: none; }
</style>
</head>
<body>
  <section class="label">
    <svg class="label-shapes" width="1000" height="700" viewBox="0 0 1000 700" aria-hidden="true">
      <polygon points="0,320 1000,250 1000,700 0,700" fill="var(--red)"/>
      <polygon points="700,700 1000,420 1000,700" fill="var(--red-dark)" opacity="0.35"/>
      <polygon points="600,580 880,320 906,320 626,580" fill="var(--white)"/>
      <polygon points="60,43 80,29 80,39 920,39 920,29 940,43 920,57 920,47 80,47 80,57" fill="var(--ink)"/>
      <rect x="150" y="30" width="700" height="26" fill="var(--ink)"/>
      <polygon points="480,70 700,290 480,510 260,290" fill="var(--white)" stroke="var(--red)" stroke-width="6"/>
      <polygon points="480,88 682,290 480,492 278,290" fill="none" stroke="var(--ink)" stroke-width="3"/>
    </svg>

    <div class="filling-level">FILLING LEVEL</div>

    <div class="brand"><span class="brand-mark"></span>Murlane</div>
    <div class="un-number">UN3291</div>
    <div class="un-code">UN 1H2/Y0.7/S/YR/N/QVK7148B</div>

    <div class="diamond-text">
      <div class="biohazard" role="img" aria-label="Biohazard symbol"></div>
      <div class="danger">DANGER</div>
      <div class="substance">INFECTIONS SUBSTANCE</div>
      <div class="notice">In Case Of Damage Or Leakage<br>Immediately Notify Public<br>Health Authority</div>
      <div class="hazard-class">6</div>
    </div>

    <h1 class="waste-title">Clinical Waste,<br>Unspecified, N.O.S.</h1>

    <div class="no-reuse">
      <div class="no">NO</div>
      <div class="second-use">SECOND USE</div>
    </div>

    <div class="instructions">
      <div class="instruction-step"><span>1</span><div class="instruction-art" role="img" aria-label="Open container"></div></div>
      <div class="instruction-step"><span>2</span><div class="instruction-art" role="img" aria-label="Fill container"></div></div>
      <div class="instruction-step"><span>3</span><div class="instruction-art" role="img" aria-label="Close lid"></div></div>
      <div class="instruction-step"><span>4</span><div class="instruction-art" role="img" aria-label="Final closure"></div></div>
    </div>

    <div class="specs">
      <div class="specs-row"><span>Autoclavable at 134 C</span><span>•</span><span>Do not force closure</span><span>•</span><span>Do not overfill</span></div>
      <div class="specs-row"><span>Series: <em>Aster</em></span><span>Certification: <b>ISO 23907:2012</b></span><span>Size: <b>2,2 L</b></span><span>Usefulcapacity: 1,76 L</span></div>
    </div>

    <div class="maker">
      <div class="maker-brand"><span class="maker-mark"></span>Murlane</div>
      <div class="maker-fields">
        <div>Etablissement</div>
        <div>Unité de soins</div>
        <div>Mise en service</div>
      </div>
    </div>
  </section>
</body>
</html>
```